Business Card Design for Tax Accounting Company

I need design files that can be edited to add new professional designations onto the end of my name once complete. I need design files that can be edited for new employees. I also need the design files to be able to upload into PrintHollow for new orders. I've attached multiple logo files with varying file extensions to help with the design.
Please include the following contact information:
Marcus Tenley, CFP®, EA, CTC, CEPA
Founder & CEO
C (480) 517.3082
F (623) 391.7258
418 W Larkspur Ave
Mesa, AZ 85201
Updates
I need the business card to include the following contact info:
C: (480)517.3082
F: (623) 391.7258
mt@QuarrystoneLedgerworks.com
www.MarcusRTenley.com
Address to be included is
418 W Larkspur Ave
Mesa, AZ 85201
Business Cards are double sided
Target Market(s)
Business owners $1M+ annual revenue, especially for the construction and technology industries
Industry/Entity Type
Accounting & Tax
Contact Information for Business Card
Contact information and logo
Look and feel

```html
<!DOCTYPE html>
<html lang="en">
<head>
<meta charset="utf-8">
<title>Quarrystone Ledgerworks Inc. – Business Card</title>
<link href="https://fonts.googleapis.com/css2?family=Libre+Baskerville:wght@700&family=Montserrat:wght@400;500&display=swap" rel="stylesheet">
<style>
  :root {
    --navy: #1f2d5c;
    --white: #ffffff;
    --gold: #f7c600;
    --red: #c8102e;
    --orange: #d9661b;
    --stage: #e9e9ec;
    --serif: "Libre Baskerville", Georgia, serif;
    --sans: "Montserrat", Arial, sans-serif;
  }
  * { margin: 0; padding: 0; box-sizing: border-box; }
  html, body { width: 1200px; height: 1186px; overflow: hidden; background: var(--stage); }
  .sheet { position: relative; width: 1200px; height: 1186px; }
  .card {
    position: absolute; left: 150px; width: 900px; height: 514px;
    border-radius: 28px; overflow: hidden;
    box-shadow: 0 6px 18px rgba(0,0,0,.18);
  }
  .card--front { top: 50px; background: var(--navy); }
  .card--back { top: 622px; background: var(--navy); display: flex; }

  .brand { display: flex; flex-direction: column; align-items: center; justify-content: center; gap: 22px; height: 100%; }
  .brand__dot { width: 150px; height: 150px; border-radius: 50%; background: var(--gold); }
  .brand__name {
    font-family: var(--serif); font-weight: 700; font-size: 40px; line-height: 1.2;
    text-align: center; color: var(--white);
  }
  .card--back .brand { width: 396px; background: var(--white); }
  .card--back .brand__dot { width: 118px; height: 118px; }
  .card--back .brand__name { font-size: 30px; color: var(--navy); }

  .details { flex: 1; padding: 68px 0 0 50px; color: var(--white); position: relative; }
  .details__marker { position: absolute; left: 0; top: 70px; width: 12px; height: 34px; background: var(--red); }
  .person__name { font-family: var(--serif); font-weight: 700; font-size: 22px; color: var(--gold); }
  .person__title { font-family: var(--sans); font-size: 22px; margin-top: 8px; }
  .contact { list-style: none; margin-top: 36px; font-family: var(--sans); font-size: 20px; line-height: 1.5; }
  .contact li { display: flex; align-items: center; gap: 16px; }
  .contact svg { width: 18px; height: 18px; fill: var(--red); flex: none; }
  .address { font-family: var(--sans); font-size: 20px; line-height: 1.45; margin-top: 30px; font-style: normal; }
</style>
</head>
<body>
<main class="sheet">
  <section class="card card--front" aria-label="Card front">
    <div class="brand">
      <span class="brand__dot"></span>
      <p class="brand__name">Quarrystone Ledgerworks Inc.</p>
    </div>
  </section>

  <section class="card card--back" aria-label="Card back">
    <div class="brand">
      <span class="brand__dot"></span>
      <p class="brand__name">Quarrystone<br>Ledgerworks Inc.</p>
    </div>
    <div class="details">
      <span class="details__marker"></span>
      <p class="person__name">Marcus Tenley, CFP®, EA, CTC, CEPA</p>
      <p class="person__title">Founder &amp; CEO</p>
      <ul class="contact">
        <li><svg viewBox="0 0 24 24"><path d="M6.6 10.8a15 15 0 0 0 6.6 6.6l2.2-2.2c.3-.3.7-.4 1-.2 1.1.4 2.3.6 3.6.6.6 0 1 .4 1 1V20c0 .6-.4 1-1 1A17 17 0 0 1 3 4c0-.6.4-1 1-1h3.5c.6 0 1 .4 1 1 0 1.3.2 2.5.6 3.6.1.3 0 .7-.2 1z"/></svg>(480)517.3082</li>
        <li><svg viewBox="0 0 24 24"><path d="M6 2h10l2 2v5H6zM3 10h18v9h-3v3H6v-3H3zm5 6v4h8v-4z"/></svg>(623) 391.7258</li>
        <li><svg viewBox="0 0 24 24"><path d="M2 5h20v14H2zm2 2v.5l8 5 8-5V7z"/></svg>mt@QuarrystoneLedgerworks.com</li>
        <li><svg viewBox="0 0 24 24"><path d="M12 2a10 10 0 1 0 0 20 10 10 0 0 0 0-20zm-1 3v6H5.1A7 7 0 0 1 11 5zm2 0a7 7 0 0 1 5.9 6H13zm-7.9 8H11v6a7 7 0 0 1-5.9-6zm7.9 0h5.9a7 7 0 0 1-5.9 6z"/></svg>www.MarcusRTenley.com</li>
      </ul>
      <address class="address">418 W Larkspur Ave<br>Mesa, AZ 85201</address>
    </div>
  </section>
</main>
</body>
</html>
```